Experienced and Professional Marriage Celebrant

I need a web design for my services as a marriage celebrant in the Sydney area. I want people to have the impression I am a modern and professional marriage celebrant who can tailor a wedding ceremony and execute the ceremony with a high level of care and accommodate and adapt to any style of wedding and personalities of couples. I like a mint and pink and black theme and I am not sure whether to use the professional photos of me, might be too stiff! But would like to see ideas you can come up with. Happy to use other photos you might have

Reason: I have haven't been able to respond as quickly as I would have liked this last week to comments so extending a few days. Thanks

```html
<!DOCTYPE html>
<html lang="en">
<head>
<meta charset="utf-8">
<title>Lena Marlow Celebrant</title>
<link href="https://fonts.googleapis.com/css2?family=Cinzel:wght@400;600&family=Arimo:wght@400;700&family=Pinyon+Script&display=swap" rel="stylesheet">
<style>
:root{
  --pink:#c95bb5;
  --pink-soft:#eec4e4;
  --pink-pale:#f7e3f2;
  --ink:#222;
  --text:#555;
  --cream:#f6f1ea;
  --pattern:#f3efe9;
  --white:#fff;
}
*{margin:0;padding:0;box-sizing:border-box}
html,body{width:1200px;height:2390px;overflow:hidden;background:var(--white)}
body{position:relative;font-family:"Arimo",Arial,sans-serif;color:var(--text)}
.abs{position:absolute}

/* hero */
.hero{left:0;top:0;width:1200px;height:585px;background:linear-gradient(90deg,#efe4d4 0%,#f4ebdf 35%,#f1ede9 55%,#e9e4df 100%)}
.hero-bouquet{left:590px;top:110px;width:520px;height:470px;border-radius:48% 45% 40% 50%;background:radial-gradient(ellipse at 50% 45%,#f3d8c0 0%,#ef9f74 45%,#e9c7a8 70%,rgba(233,228,223,0) 100%)}
.topbar{left:0;top:0;width:1200px;height:105px;background:rgba(255,255,255,.55)}
.logo{left:190px;top:56px;font-family:"Cinzel",serif;font-size:26px;line-height:32px;color:var(--ink);letter-spacing:.5px;white-space:nowrap}
.tagline{left:284px;top:132px;font-family:"Cinzel",serif;font-size:13px;letter-spacing:2.5px;color:var(--ink);white-space:nowrap}
.nav{left:622px;top:0;height:105px;display:flex;align-items:center;list-style:none}
.nav li{font-size:14px;letter-spacing:1px;color:#777;padding:0 22px;height:105px;line-height:122px}
.nav li.active{background:var(--pink);color:var(--white);padding:0 14px}
.portrait{left:310px;top:170px;width:164px;height:164px;border-radius:50%;border:4px solid #2a2a2a;background:linear-gradient(160deg,#8c6a5a,#b89ad0)}
.hero-quote{left:255px;top:360px;width:290px;font-family:"Pinyon Script",cursive;font-size:23px;line-height:33px;color:var(--pink);text-align:center}
.love-mark{left:340px;top:470px;width:110px;height:36px;border-radius:18px;background:rgba(0,0,0,.08)}

/* section heads */
.sec-title{left:0;width:1200px;font-family:"Cinzel",serif;font-weight:400;font-size:25px;letter-spacing:2px;color:var(--ink);text-align:center}
.divider{left:545px;width:132px;height:20px;z-index:2}
.sub{left:0;width:1200px;font-size:14px;color:var(--pink);text-align:center}

/* gallery */
.pattern{left:0;width:1200px;background:var(--pattern)}
.frame{border:7px solid var(--pink-soft);background:var(--white);padding:6px}
.frame div{width:100%;height:100%}
.dots{left:555px;top:1116px;display:flex;gap:8px}
.dots span{width:12px;height:12px;border-radius:50%;background:#d8d4d0}
.dots span.on{background:var(--pink)}

/* work */
.work-band{left:0;top:1268px;width:1200px;height:372px;background:linear-gradient(90deg,#cbbfb6,#e9e3de 30%,#efeae6 70%,#c9bfba)}
.work-card{left:170px;top:1268px;width:875px;height:352px;background:var(--white)}
.service{top:1328px;width:190px;text-align:center}
.service svg{display:block;margin:0 auto 12px;height:70px}
.service h3{font-weight:400;font-size:15px;color:#333;letter-spacing:.5px;margin-bottom:16px}
.service p{font-size:12.5px;line-height:15px;color:#666;margin-bottom:12px}
.btn{display:inline-block;background:var(--pink);color:var(--white);font-size:11px;padding:5px 10px;letter-spacing:1px}

/* testimonial */
.quote-band{left:0;top:1822px;width:1200px;height:258px;background:linear-gradient(90deg,#4a3a33 0%,#9a8377 30%,#e9d6c8 60%,#f2e3d8 100%)}
.quote-box{left:207px;top:1872px;width:798px;height:103px;background:rgba(255,255,255,.55)}
.quote-mark{left:222px;top:1868px}
.quote-text{left:310px;top:1900px;width:650px;font-size:15px;line-height:20px;color:var(--pink);text-align:center}
.client{left:600px;top:1990px;width:300px;font-family:"Pinyon Script",cursive;font-size:24px;color:var(--pink);text-align:center}
.client-role{left:600px;top:2027px;width:300px;font-family:"Cinzel",serif;font-size:11px;letter-spacing:2px;color:#444;text-align:center}

/* footer */
.footer{left:0;top:2080px;width:1200px;height:250px;background:var(--pattern)}
.foot-logo{left:222px;top:2106px;font-family:"Cinzel",serif;font-size:17px;color:var(--pink);white-space:nowrap}
.foot-nav{left:234px;top:2150px;list-style:none;font-size:14px;line-height:20px;color:#444;letter-spacing:.5px}
.follow{left:234px;top:2268px;font-family:"Cinzel",serif;font-size:10px;color:#444}
.social{left:234px;top:2286px;display:flex;gap:6px}
.social span{width:20px;height:20px;background:var(--pink-soft)}
.foot-head{font-family:"Cinzel",serif;font-size:11px;color:#333;white-space:nowrap}
.tweet{left:470px;width:250px;font-size:12.5px;line-height:15px;color:#555}
.tweet .dot{position:absolute;left:0;top:2px;width:14px;height:14px;border-radius:50%;background:var(--pink)}
.tweet p{margin-left:26px}
.tweet .when{color:var(--pink);font-weight:700;font-size:11px;margin-top:3px}
.field{display:flex}
.field span{width:180px;height:22px;background:var(--pink-pale);font-size:11px;color:#666;padding:5px 10px}
.field b{width:24px;height:22px;background:var(--pink);color:var(--white);font-size:10px;text-align:center;line-height:22px;margin-left:2px}
.contact-bar{left:0;top:2330px;width:1200px;height:60px;background:var(--pink);color:var(--white)}
.contact-bar .lbl{position:absolute;top:22px;font-size:13px}
.contact-bar .val{position:absolute;top:15px;font-size:22px;letter-spacing:.5px;white-space:nowrap}
.contact-bar .sep{position:absolute;left:590px;top:12px;width:1px;height:36px;background:rgba(255,255,255,.4)}
</style>
</head>
<body>

<header>
  <div class="abs hero" role="img" aria-label="Photo of a bride in a white dress holding a bouquet"></div>
  <div class="abs hero-bouquet" role="img" aria-label="Bouquet of peach roses and orange lilies"></div>
  <div class="abs topbar"></div>
  <div class="abs logo">Lena Marlow Celebrant</div>
  <div class="abs tagline">MARRIAGE CELEBRANT</div>
  <ul class="abs nav">
    <li class="active">HOME</li><li>WEDDINGS</li><li>GALLERY</li><li>FAQ</li><li>NEWS</li>
  </ul>
  <div class="abs portrait" role="img" aria-label="Portrait photo of the celebrant"></div>
  <p class="abs hero-quote">Tiam id loctus eu nibh cursus blandit. Donec iaculis interdum sapien</p>
  <div class="abs love-mark" role="img" aria-label="Infinity love ornament"></div>
</header>

<section class="gallery">
  <h2 class="abs sec-title" style="top:648px">GALLERY</h2>
  <svg class="abs divider" style="top:680px" viewBox="0 0 132 20"><line x1="0" y1="10" x2="54" y2="10" stroke="#bbb"/><line x1="78" y1="10" x2="132" y2="10" stroke="#bbb"/><path d="M66 17 L58 9 A4 4 0 0 1 66 5 A4 4 0 0 1 74 9 Z" fill="var(--pink)"/></svg>
  <p class="abs sub" style="top:718px">Lorem ipsum dolor sit amet, consectetur adipisicing elit</p>
  <div class="abs pattern" style="top:760px;height:408px" role="img" aria-label="Soft floral pattern background"></div>
  <div class="abs frame" style="left:155px;top:793px;width:207px;height:292px"><div role="img" aria-label="Photo of a ceremony by the water" style="background:linear-gradient(180deg,#6f97c2,#c9b9c6 55%,#4d5366)"></div></div>
  <div class="abs frame" style="left:405px;top:793px;width:381px;height:292px"><div role="img" aria-label="Photo of the wedding party walking on a beach" style="background:linear-gradient(180deg,#5d8ac9 0%,#9ec0e4 45%,#b08a66 70%,#7e5e44)"></div></div>
  <div class="abs frame" style="left:828px;top:793px;width:220px;height:292px"><div role="img" aria-label="Photo of the couple embracing at the shore" style="background:linear-gradient(180deg,#a9b9cc,#8a8f7d 50%,#3d3a3a 75%,#c9c4bd)"></div></div>
  <div class="abs dots"><span></span><span></span><span class="on"></span><span></span><span></span><span></span></div>
</section>

<section class="work">
  <h2 class="abs sec-title" style="top:1214px">MY WORK</h2>
  <svg class="abs divider" style="top:1244px" viewBox="0 0 132 20"><line x1="0" y1="10" x2="54" y2="10" stroke="#bbb"/><line x1="78" y1="10" x2="132" y2="10" stroke="#bbb"/><path d="M66 17 L58 9 A4 4 0 0 1 66 5 A4 4 0 0 1 74 9 Z" fill="var(--pink)"/></svg>
  <div class="abs work-band" role="img" aria-label="Blurred photo of a wedding reception table"></div>
  <div class="abs work-card"></div>

  <div class="abs service" style="left:190px">
    <svg viewBox="0 0 60 70"><circle cx="30" cy="12" r="10" fill="var(--pink)"/><path d="M8 70 V36 Q8 26 18 26 H42 Q52 26 52 36 V70 Z" fill="var(--pink)"/><path d="M27 27 H33 L35 52 L30 58 L25 52 Z" fill="#fff"/></svg>
    <h3>Professional Celebrant</h3>
    <p>Lorem ipsum dolor sit amet, consectetur adipisicing elit, sed do eiusmod tempor incre magna aliqua.</p>
    <span class="btn">MORE</span>
  </div>
  <div class="abs service" style="left:412px">
    <svg viewBox="0 0 60 70"><path d="M18 30 Q18 6 36 6 Q54 6 54 28 Q54 40 44 48 Q38 54 38 62 Q38 68 30 68 Q22 68 22 60" fill="none" stroke="var(--pink)" stroke-width="6" stroke-linecap="round"/><path d="M30 30 Q30 18 38 18 Q46 18 44 30 Q42 36 36 38" fill="none" stroke="var(--pink)" stroke-width="5" stroke-linecap="round"/></svg>
    <h3>Awesome PA system</h3>
    <p>Lorem ipsum dolor sit amet, consectetur adipisicing elit, sed do eiusmod tempor incididunt ut labore et dolore magna aliqua.</p>
    <span class="btn">MORE</span>
  </div>
  <div class="abs service" style="left:634px">
    <svg viewBox="0 0 80 70"><circle cx="28" cy="42" r="19" fill="none" stroke="var(--pink)" stroke-width="6"/><circle cx="52" cy="42" r="19" fill="none" stroke="var(--pink)" stroke-width="6"/><path d="M40 18 L33 11 A4 4 0 0 1 40 6 A4 4 0 0 1 47 11 Z" fill="var(--pink)"/></svg>
    <h3>All about marriage</h3>
    <p>Lorem ipsum dolor sit amet, consectetur adipisicing elit, sed do eiusmod temp.</p>
    <span class="btn">MORE</span>
  </div>
  <div class="abs service" style="left:845px">
    <svg viewBox="0 0 70 70"><path d="M5 20 L35 4 L65 20 Z" fill="var(--pink)"/><rect x="5" y="20" width="60" height="6" fill="var(--pink)"/><rect x="10" y="26" width="4" height="40" fill="var(--pink)"/><rect x="56" y="26" width="4" height="40" fill="var(--pink)"/><rect x="33" y="26" width="4" height="14" fill="var(--pink)"/><path d="M22 40 H46 L44 52 H26 Z" fill="var(--pink)"/><rect x="5" y="64" width="60" height="5" fill="var(--pink)"/></svg>
    <h3>Loads of fun</h3>
    <p>Lorem ipsum dolor sit amet, consectetur adipisicing elit, sed do eiusmod tempor incididunt ut labore et dolore</p>
    <span class="btn">MORE</span>
  </div>
</section>

<section class="testimonials">
  <h2 class="abs sec-title" style="top:1694px;line-height:34px">WHAT MY CLIENTS SAY<br>ABOUT ME</h2>
  <svg class="abs divider" style="top:1772px" viewBox="0 0 132 20"><line x1="0" y1="10" x2="54" y2="10" stroke="#bbb"/><line x1="78" y1="10" x2="132" y2="10" stroke="#bbb"/><path d="M66 17 L58 9 A4 4 0 0 1 66 5 A4 4 0 0 1 74 9 Z" fill="var(--pink)"/></svg>
  <div class="abs quote-band" role="img" aria-label="Photo of a bride's dress and bouquet in soft light"></div>
  <div class="abs quote-box"></div>
  <svg class="abs quote-mark" width="78" height="70" viewBox="0 0 78 70"><path d="M2 4 H34 V36 Q34 60 10 66 L8 58 Q20 52 20 40 H2 Z" fill="var(--pink-soft)"/><path d="M42 4 H74 V36 Q74 60 50 66 L48 58 Q60 52 60 40 H42 Z" fill="var(--pink-soft)"/></svg>
  <p class="abs quote-text">Dolor sit amet, consectetur adipisicing elit, sed do eiusmod tempor incididunt ut labore et dolore magna aliqua.</p>
  <div class="abs client">Clara Bennet</div>
  <div class="abs client-role">BRIDE</div>
</section>

<footer>
  <div class="abs footer" role="img" aria-label="Soft floral pattern background"></div>
  <div class="abs foot-logo">Lena Marlow Celebrant</div>
  <ul class="abs foot-nav"><li>HOME</li><li>WEDDINGS</li><li>GALLERY</li><li>FAQ</li><li>NEWS</li></ul>
  <div class="abs follow">FALOW ME ON</div>
  <div class="abs social"><span></span><span></span><span></span><span></span></div>

  <div class="abs foot-head" style="left:495px;top:2124px">NEWS ON TWEETER</div>
  <div class="abs tweet" style="top:2146px"><span class="dot"></span><p>Lorem ipsum dolor sit amet, consectetur. Lorem ipsum dolor sit amet, consectetur.</p><p class="when">3 days ago</p></div>
  <div class="abs tweet" style="top:2222px"><span class="dot"></span><p>Lorem ipsum dolor sit amet, consectetur. Lorem ipsum dolor sit amet, consectetur.</p><p class="when">3 days ago</p></div>

  <div class="abs foot-head" style="left:812px;top:2124px">FEEL FREE TO SIGNUP FOR MY NEWSLETTER</div>
  <div class="abs field" style="left:812px;top:2144px"><span>Name</span></div>
  <div class="abs field" style="left:812px;top:2182px"><span>E-mail</span><b>GO</b></div>
  <div class="abs" style="left:812px;top:2240px;font-size:11px;color:#444">To unsubscribe enter you email address</div>
  <div class="abs field" style="left:812px;top:2262px"><span>E-mail</span><b>GO</b></div>

  <div class="abs contact-bar">
    <span class="lbl" style="left:308px">Phone:</span>
    <span class="val" style="left:372px">+1 800 555 0142</span>
    <span class="sep"></span>
    <span class="lbl" style="left:632px">Email:</span>
    <span class="val" style="left:695px">lenamarlow.celebrant@mail.example</span>
  </div>
</footer>

</body>
</html>
```